CareVantRx business cards

We need a business card design that we could customize as needed for employees. We will need space for Name, Title, 1-2 phone numbers and email address.

We are a Pharmacy Benefits Management (PBM) company for hospice agencies and beginning a nationwide expansion. Attached is a vector file of our logo.

Cards can be single or double sided.

Industry/Entity Type

Business

```html
<!DOCTYPE html>
<html lang="en">
<head>
<meta charset="utf-8">
<title>CareVantRx Business Card</title>
<link href="https://fonts.googleapis.com/css2?family=Open+Sans:wght@400;600;700&display=swap" rel="stylesheet">
<style>
  :root {
    --brand-blue: #1b5fa3;
    --brand-green: #99cb67;
    --rule-green: #c9e2ad;
    --paper: #ffffff;
  }
  html, body {
    margin: 0;
    padding: 0;
    overflow: hidden;
    background: var(--paper);
  }
  .card {
    position: relative;
    width: 1200px;
    height: 686px;
    background: var(--paper);
    overflow: hidden;
    font-family: "Open Sans", Arial, sans-serif;
  }
  .brand {
    position: absolute;
    left: 78px;
    top: 189px;
    height: 68px;
    display: flex;
    align-items: center;
    gap: 18px;
  }
  .brand-mark {
    width: 68px;
    height: 68px;
    background: var(--brand-green);
    border-radius: 6px;
  }
  .brand-name {
    font-size: 62px;
    font-weight: 600;
    color: var(--brand-blue);
    letter-spacing: -1px;
    line-height: 1;
  }
  .band-left {
    position: absolute;
    left: 0;
    top: 365px;
    width: 574px;
    height: 102px;
    background: var(--brand-green);
  }
  .band-right {
    position: absolute;
    left: 1112px;
    top: 365px;
    width: 88px;
    height: 102px;
    background: var(--brand-green);
  }
  .identity {
    position: absolute;
    right: calc(1200px - 853px);
    top: 366px;
    text-align: right;
  }
  .person-name {
    margin: 0;
    font-size: 38.5px;
    font-weight: 700;
    color: var(--brand-blue);
    line-height: 49px;
    white-space: nowrap;
  }
  .person-title {
    margin: 0;
    font-size: 38.5px;
    font-weight: 700;
    color: var(--brand-green);
    line-height: 49px;
  }
  .divider {
    position: absolute;
    left: 877px;
    top: 365px;
    width: 1.5px;
    height: 102px;
    background: var(--rule-green);
  }
  .contact {
    position: absolute;
    right: calc(1200px - 1092px);
    top: 374px;
    text-align: right;
    color: var(--brand-blue);
    font-weight: 400;
    white-space: nowrap;
  }
  .contact-phone {
    margin: 0;
    font-size: 22.5px;
    line-height: 25px;
  }
  .contact-email {
    margin: 1px 0 0;
    font-size: 15.5px;
    line-height: 20px;
  }
</style>
</head>
<body>
  <main class="card">
    <div class="brand">
      <div class="brand-mark"></div>
      <span class="brand-name">CareVantRx</span>
    </div>

    <div class="band-left"></div>

    <div class="identity">
      <p class="person-name">Daniel Mercer</p>
      <p class="person-title">CEO</p>
    </div>

    <div class="divider"></div>

    <div class="contact">
      <p class="contact-phone">555.204.8137 (C)</p>
      <p class="contact-phone">555.316.9025 (O)</p>
      <p class="contact-email">daniel@carevantrx.com</p>
    </div>

    <div class="band-right"></div>
  </main>
</body>
</html>
```